Online Psychology Practice needs business cards.

Online Psychology service needs business cards. Have own logo- please see uploaded. I have other file formats if you need (not sure one needed?)

Details for Business Card:
Fiona Kettlewood
Clinical Psychologist BPsych, BPsych (Hons), MPsych (Clin), MAPS
T: 0457260714 | F: 08 71526804
E: hello@harbourlightmindcarestudio.com.au
W: harbourlightmindcarestudio.com.au

Industry/Entity Type

Health

Contact Information for Business Card

Logo plus details above (couldn't write in this section)

```html
<!DOCTYPE html>
<html lang="en">
<head>
<meta charset="utf-8">
<title>Harbourlight Mindcare Studio – Business Cards</title>
<link rel="stylesheet" href="https://fonts.googleapis.com/css2?family=Cinzel:wght@500&family=Jost:ital,wght@0,400;0,500;1,400&display=swap">
<style>
  :root {
    --teal: #5aabc3;
    --navy: #1f4e7a;
    --paper: #ffffff;
    --stage: #ffffff;
    --ink-light: #ffffff;
  }
  * { margin: 0; padding: 0; box-sizing: border-box; }
  html, body {
    width: 1200px; height: 1200px; overflow: hidden;
    background: var(--stage);
    font-family: "Jost", sans-serif;
  }
  .card {
    position: absolute;
    left: 190px;
    width: 830px; height: 473px;
    background: var(--paper);
    box-shadow: 6px 10px 22px rgba(0,0,0,0.16);
    overflow: hidden;
  }
  .card--front { top: 91px; }
  .card--back { top: 623px; }

  /* Front */
  .front-brand {
    position: absolute; left: 0; right: 0; top: 170px;
    display: flex; flex-direction: column; align-items: center; gap: 22px;
  }
  .brand-dot {
    width: 112px; height: 112px; border-radius: 50%;
    background: var(--navy);
  }
  .brand-name {
    font-family: "Jost", sans-serif;
    font-weight: 500;
    color: var(--navy);
    text-transform: uppercase;
    letter-spacing: 2px;
    font-size: 17px;
    text-align: center;
    line-height: 1.2;
  }
  .front-band {
    position: absolute; left: 0; right: 0; bottom: 0;
    height: 102px; background: var(--teal);
    display: flex; align-items: center; justify-content: center;
  }
  .website {
    color: var(--ink-light); font-size: 16px; letter-spacing: 0.2px;
  }

  /* Back */
  .back-panel {
    position: absolute; left: 0; right: 0; top: 0;
    height: 370px; background: var(--teal);
    color: var(--ink-light);
  }
  .person-name {
    position: absolute; right: 38px; top: 36px;
    font-family: "Cinzel", serif; font-weight: 500;
    font-size: 36px; letter-spacing: 0.5px;
  }
  .credentials {
    position: absolute; right: 38px; top: 108px;
    text-align: right; font-style: italic; font-size: 22px; line-height: 28px;
  }
  .contact {
    position: absolute; left: 40px; top: 285px;
    font-size: 19px; line-height: 30px;
  }
  .contact-row { display: flex; align-items: center; gap: 10px; }
  .contact-row + .contact-row { margin-top: 0; }
  .contact-item { display: inline-flex; align-items: center; gap: 10px; margin-right: 18px; }
  .icon { width: 24px; height: 22px; fill: var(--ink-light); }
  .back-footer {
    position: absolute; left: 0; right: 0; bottom: 0; height: 103px;
    display: flex; align-items: center; justify-content: space-between;
    padding: 0 40px;
  }
  .brand-dot--small { width: 60px; height: 60px; }
  .brand-name--small { font-size: 13px; letter-spacing: 1.5px; text-align: right; }
</style>
</head>
<body>

<section class="card card--front">
  <div class="front-brand">
    <div class="brand-dot"></div>
    <div class="brand-name">Harbourlight<br>Mindcare Studio</div>
  </div>
  <div class="front-band">
    <span class="website">harbourlightmindcarestudio.com.au</span>
  </div>
</section>

<section class="card card--back">
  <div class="back-panel">
    <h1 class="person-name">Fiona Kettlewood</h1>
    <p class="credentials">Clinical Psychologist BPsych,<br>BPsych (Hons),<br>MPsych (Clin),<br>MAPS</p>
    <div class="contact">
      <div class="contact-row">
        <span class="contact-item">
          <svg class="icon" viewBox="0 0 24 24" aria-hidden="true"><path d="M6.6 10.8a15.1 15.1 0 0 0 6.6 6.6l2.2-2.2a1 1 0 0 1 1-.25 11.4 11.4 0 0 0 3.6.57 1 1 0 0 1 1 1V20a1 1 0 0 1-1 1A17 17 0 0 1 3 4a1 1 0 0 1 1-1h3.5a1 1 0 0 1 1 1c0 1.25.2 2.45.57 3.57a1 1 0 0 1-.25 1z"/></svg>
          0457260714
        </span>
        <span class="contact-item">
          <svg class="icon" viewBox="0 0 24 24" aria-hidden="true"><path d="M6 2h12v6H6zM3 9h18a1 1 0 0 1 1 1v8h-4v4H6v-4H2v-8a1 1 0 0 1 1-1zm5 8v3h8v-3zm10-6a1 1 0 1 0 0 2 1 1 0 0 0 0-2z"/></svg>
          08 71526804
        </span>
      </div>
      <div class="contact-row">
        <span class="contact-item">
          <svg class="icon" viewBox="0 0 24 20" aria-hidden="true"><path d="M1 2h22v16H1zm2 2.2V16h18V4.2l-9 6.3z"/></svg>
          hello@harbourlightmindcarestudio.com.au
        </span>
      </div>
    </div>
  </div>
  <div class="back-footer">
    <div class="brand-dot brand-dot--small"></div>
    <div class="brand-name brand-name--small">Harbourlight<br>Mindcare Studio</div>
  </div>
</section>

</body>
</html>
```